Collage: Kunden in Coaching und Organisationsberatung

Ich brauche eine jederzeit mit herkömmlichen Programmen bearbeitbare Vorlage, um in sozialen Medien meine Kunden vorstellen zu können - damit zu erklären, wie Coaching und Organisationsberatung wirken kann. Diese Persona sollen in einer Collage mit passenden Bildern und Texten präsentiert werden können. Als grafische Orientierung kann meine Homepage https://www.plavisno.at/ dienen. Meine Farbcodes sind auf der Webseite - sprich digital RGB: Blau: #739fc7, Grün: #b8c830 und Orange: #cc610a; Im Print also CMYK: Blau: 70/20/10/0, Grün: 0/10/100/0 und Orange: 0/68/100/0; Texte sollen in folgender Länge Platz finden - diese Info dient nur zur Größenabschätzung der Platzhalter. Der Rest kann frei mit Bildern, Symbolen, ... gestaltet werden.
Textbeispiel 1:
Helga – Führungskraft mit Ambitionen und Herausforderungen
Alter: 42 Jahre
Funktion: Bereichsleiterin Finanzen in einem großen Dienstleistungsunternehmen
Lebenssituation: Verheiratet, zwei Kinder (Gymnasium, Unterstufe), Partner arbeitet als technischer Zeichner
🎯 Ziele & 🧭 Motive
• Will sich als moderne Führungskraft etablieren – mit Haltung, Vertrauen und Eigenverantwortung
• Strebt eine konstruktive, offene Kommunikation in ihrem Bereich an
• Möchte ihren Managementstil von operativer Detailarbeit hin zur strategischen Führung weiterentwickeln
• Sucht nach Balance zwischen Beruf, Familie und persönlichen Bedürfnissen
⚠️ Herausforderungen & Belastungen
• Übergang von Kollegin zu Vorgesetzter: Beziehungskonflikte und Rollenklarheit
• Kommunikationskultur im Team ist verschlossen und wenig kooperativ
• Hoher Anspruch an sich selbst – und an andere
• Rückfall in operative Aufgaben → Zeitdruck & Energieverlust
• Entscheidungsschwierigkeiten durch komplexe Abstimmungen und fehlende Klarheit über Stakeholder
• Innere Spannung zwischen Führungsanspruch und fehlendem methodischem Rüstzeug
💬 Typische Aussagen
• „Ich will nicht führen wie mein Vorgänger – das geht heute anders.“
• „Ich will, dass die Leute Verantwortung übernehmen und nicht nur ausführen.“
• „Manchmal bin ich zu ungeduldig – aber ich habe einfach keine Zeit für Umwege.“
• „Ich muss weg von der Detailarbeit – aber wie schaffe ich das wirklich?“
📌 Entwicklungsbedarfe
• Coaching zur Selbstklärung und Rollenentwicklung
• Training zu Kommunikation in Führung, Feedback- und Konfliktkultur
• Impulse zur Reflexion über Führungshaltung und Teamsteuerung
• Unterstützung im Aufbau eines kollaborativen Netzwerks innerhalb der Organisation
📣 Zielgruppenansprache (Voxtera-Kontext)
Diese Persona spricht Führungskräfte an, die:
• neu in ihrer Rolle sind (meist durch schnellen Aufstieg)
• den Willen zur Veränderung mitbringen, aber noch nicht das passende Werkzeug
• zwischen strategischem Anspruch und operativem Alltag aufgerieben werden
• Kommunikation, Führung und Selbstführung gleichzeitig lernen und leben wollen
Textbeispiel 2:
Herbert
Persona: Herbert – Fachlich stark, persönlich überfordert
Alter: 36 Jahre
Funktion: Bilanzbuchhalter in einer mittelgroßen Spedition
Position: Formal als Abteilungsleiter geführt – ohne kommunizierte Führungsverantwortung
Lebenssituation: Lebt allein, gelegentliche Beziehungserfahrungen
🎯 Ziele & 🧭 Motive
• Wünscht sich Stabilität, Struktur und fachlich saubere Arbeitsprozesse
• Möchte gute, fehlerfreie Arbeit leisten und professionell wahrgenommen werden
• Hat sich für diesen Job entschieden, um mehr Lebensqualität zu gewinnen
• Sehnt sich nach Klarheit in Rollen, Zuständigkeiten und Abläufen
• Ungeklärte Führungsrolle: Der Titel „Abteilungsleiter*“ verunsichert – es fehlt eine explizite Einordnung
• Überlastung durch chaotische Prozesse und laufende Systemumstellung
• Fehlende Unterstützung im Team – insbesondere durch eine überforderte Kollegin
• Schwierigkeiten, Grenzen zu setzen oder Klarheit einzufordern – v. a. gegenüber Führungskraft und Kolleg*innen
• Perfektionismus führt zu Überstunden, Schlafproblemen und emotionaler Erschöpfung
• Geringe Sichtbarkeit im Betrieb – kaum Kommunikation außerhalb des Büros
• Hohes Bedürfnis nach Kontrolle steht einem agilen Umfeld entgegen
💬 Typische Aussagen
• „Ich bin kein Abteilungsleiter – ich habe das nie gewollt.“
• „Ich will einfach gute Arbeit machen – aber so geht das nicht.“
• „Ich habe keine Zeit, das Chaos zu ordnen – ich bin zu sehr damit beschäftigt, es auszuhalten.“
• „Coaching? Vielleicht bringt es ja wenigstens etwas Struktur in meine Gedanken.“
📌 Entwicklungsbedarfe
• Klärung der eigenen beruflichen Rolle und Abgrenzung zur Führungsverantwortung
• Unterstützung beim Umgang mit Unklarheit und Perfektionismus
• Stärkung der Selbstführung und Kommunikation im System
• Strukturierungshilfen im Arbeitsalltag – Priorisierung, Delegation, Nein-Sagen
• Entlastung durch Reflexion – Reduktion von Selbstüberforderung
• Ermutigung zur Klärung mit Führungskraft (z. B. über ein geleitetes Gespräch oder systemisches Rollenmodell)
Diese Persona spricht Mitarbeiter*innen an, die:
• fachlich sehr kompetent, aber systemisch überfordert sind
• sich in unklaren Rollen- und Erwartungsstrukturen wiederfinden
• zwischen Anspruch und Wirklichkeit leiden
• sich nach Struktur, Sicherheit und professioneller Entlastung sehnen
• Coaching als „letzte Möglichkeit“ sehen, ihre Gedanken zu ordnen und Klarheit zu gewinnen
LG und danke für die Vorschläge

```html
<!DOCTYPE html>
<html lang="de">
<head>
<meta charset="utf-8">
<title>Persona Helga – plavisno Entwicklungsberatung</title>
<link href="https://fonts.googleapis.com/css2?family=Open+Sans:wght@400;600;700&family=Raleway:ital,wght@0,500;0,600;0,700;1,500&display=swap" rel="stylesheet">
<style>
  :root{
    --blue:#739fc7;
    --blue-dark:#3f6f9e;
    --blue-deep:#27527f;
    --green:#b8c830;
    --orange:#cc610a;
    --ink:#3a4654;
    --muted:#5d6a78;
    --paper:#ffffff;
  }
  *{box-sizing:border-box;margin:0;padding:0}
  html,body{width:849px;height:1200px;overflow:hidden;background:var(--paper)}
  body{font-family:"Open Sans",Arial,sans-serif;color:var(--ink);position:relative}

  .hero-illustration{position:absolute;left:0;top:0;width:523px;height:405px;
    background:linear-gradient(180deg,#bcdcf2 0%,#e3f1fa 60%,#fbfdff 100%)}
  .stripe-band{position:absolute;left:523px;top:0;width:326px;height:750px;
    background:linear-gradient(135deg,#a9cbe8 0%,#6697c9 50%,#2f6aa6 100%)}
  .stripe-edge{position:absolute;left:806px;top:750px;width:43px;height:450px;
    background:linear-gradient(180deg,#6697c9,#b3d1ec)}
  .photo{position:absolute;border:4px solid var(--paper)}
  .photo-portrait{left:665px;top:0;width:184px;height:158px;background:linear-gradient(160deg,#d9c7b3,#eceff2)}
  .photo-chart{left:595px;top:272px;width:254px;height:180px;background:linear-gradient(135deg,#0d2d5a,#2a6bb3)}
  .photo-phone{left:538px;top:468px;width:200px;height:145px;background:linear-gradient(135deg,#3b5d86,#9bb6d1)}

  .brand{position:absolute;left:80px;top:418px;width:420px;text-align:center}
  .brand-name{font-family:"Raleway",sans-serif;font-weight:500;font-size:74px;letter-spacing:2px;color:var(--blue-deep);line-height:1}
  .brand-sub{font-family:"Raleway",sans-serif;font-style:italic;font-weight:500;font-size:27px;color:var(--blue-deep);margin-top:6px;line-height:1.1}
  .brand-tag{font-family:"Raleway",sans-serif;font-style:italic;font-size:16px;color:var(--blue-deep);margin-top:2px}

  .persona-title{position:absolute;left:58px;top:600px;width:470px;font-family:"Raleway",sans-serif;font-weight:700;font-size:25px;line-height:31px;color:var(--blue-deep)}
  .persona-facts{position:absolute;left:58px;top:674px;width:450px;font-size:9.5px;line-height:13px}
  .persona-facts b{font-weight:700}

  .column{position:absolute;top:772px}
  .column-left{left:58px;width:450px}
  .column-right{left:540px;width:262px}
  .section{margin-bottom:18px}
  .section-head{display:flex;align-items:center;gap:7px;font-family:"Raleway",sans-serif;font-weight:700;font-size:11px;color:var(--blue-dark);margin-bottom:6px}
  .section-icon{width:10px;height:10px;border-radius:2px;background:var(--orange);flex:none}
  .section-icon.green{background:var(--green)}
  .section-icon.blue{background:var(--blue)}
  .section-intro{font-size:9.5px;line-height:13px;margin-bottom:3px}
  .bullets{list-style:none;font-size:9.5px;line-height:13px}
  .bullets li{position:relative;padding-left:12px;margin-bottom:2.5px}
  .bullets li::before{content:"";position:absolute;left:1px;top:5px;width:4px;height:4px;border-radius:50%;background:var(--orange)}
  .bullets b{font-weight:700}
</style>
</head>
<body>
  <div class="hero-illustration" role="img" aria-label="Illustration: Personen steigen über Stufen einen Berggipfel hinauf, Himmel mit Wolken"></div>
  <div class="stripe-band" role="img" aria-label="Dekoratives blaues Diagonalmuster"></div>
  <div class="stripe-edge" role="img" aria-label="Dekoratives blaues Diagonalmuster"></div>
  <div class="photo photo-portrait" role="img" aria-label="Porträtfoto einer Führungskraft"></div>
  <div class="photo photo-chart" role="img" aria-label="Foto: digitale Wachstumsgrafik"></div>
  <div class="photo photo-phone" role="img" aria-label="Foto: Hände mit Smartphone"></div>

  <header class="brand">
    <div class="brand-name">plavisno</div>
    <div class="brand-sub">Entwicklungsberatung</div>
    <div class="brand-tag">Inspiration · Lernen · Wachstum</div>
  </header>

  <h1 class="persona-title">Helga – Führungskraft mit Ambitionen und Herausforderungen</h1>
  <div class="persona-facts">
    <p><b>Alter:</b> 42 Jahre</p>
    <p><b>Funktion:</b> Bereichsleiterin Finanzen in einem großen Dienstleistungsunternehmen</p>
    <p><b>Lebenssituation:</b> Verheiratet, zwei Kinder (Gymnasium, Unterstufe), Partner arbeitet als technischer Zeichner</p>
  </div>

  <main>
    <div class="column column-left">
      <section class="section">
        <div class="section-head"><span class="section-icon"></span>Ziele &amp; Motive</div>
        <ul class="bullets">
          <li>Will sich als moderne Führungskraft etablieren – mit Haltung, Vertrauen und Eigenverantwortung</li>
          <li>Strebt eine konstruktive, offene Kommunikation in ihrem Bereich an</li>
          <li>Möchte ihren Managementstil von operativer Detailarbeit hin zur strategischen Führung weiterentwickeln</li>
          <li>Sucht nach Balance zwischen Beruf, Familie und persönlichen Bedürfnissen</li>
        </ul>
      </section>
      <section class="section">
        <div class="section-head"><span class="section-icon"></span>Herausforderungen &amp; Belastungen</div>
        <ul class="bullets">
          <li>Übergang von Kollegin zu Vorgesetzter: Beziehungskonflikte und Rollenklarheit</li>
          <li>Kommunikationskultur im Team ist verschlossen und wenig kooperativ</li>
          <li>Hoher Anspruch an sich selbst – und an andere</li>
          <li>Rückfall in operative Aufgaben → Zeitdruck &amp; Energieverlust</li>
          <li>Entscheidungsschwierigkeiten durch komplexe Abstimmungen und fehlende Klarheit über Stakeholder</li>
          <li>Innere Spannung zwischen Führungsanspruch und fehlendem methodischem Rüstzeug</li>
        </ul>
      </section>
    </div>

    <div class="column column-right">
      <section class="section">
        <div class="section-head"><span class="section-icon blue"></span>Typische Aussagen</div>
        <ul class="bullets">
          <li>„Ich will nicht führen wie mein Vorgänger – das geht heute anders.“</li>
          <li>„Ich will, dass die Leute Verantwortung übernehmen und nicht nur ausführen.“</li>
          <li>„Manchmal bin ich zu ungeduldig – aber ich habe einfach keine Zeit für Umwege.“</li>
          <li>„Ich muss weg von der Detailarbeit – aber wie schaffe ich das wirklich?“</li>
        </ul>
      </section>
      <section class="section">
        <div class="section-head"><span class="section-icon green"></span>Entwicklungsbedarfe</div>
        <ul class="bullets">
          <li>Coaching zur Selbstklärung und Rollenentwicklung</li>
          <li>Training zu Kommunikation in Führung, Feedback- und Konfliktkultur</li>
          <li>Impulse zur Reflexion über Führungshaltung und Teamsteuerung</li>
          <li>Unterstützung im Aufbau eines kollaborativen Netzwerks innerhalb der Organisation</li>
        </ul>
      </section>
      <section class="section">
        <div class="section-head"><span class="section-icon"></span>Zielgruppenansprache (Voxtera-Kontext)</div>
        <p class="section-intro">Diese Persona spricht Führungskräfte an, die:</p>
        <ul class="bullets">
          <li><b>neu in ihrer Rolle</b> sind (meist durch schnellen Aufstieg)</li>
          <li>den <b>Willen zur Veränderung</b> mitbringen, aber noch nicht das passende Werkzeug</li>
          <li><b>zwischen strategischem Anspruch und operativem Alltag</b> aufgerieben werden</li>
          <li><b>Kommunikation, Führung und Selbstführung</b> gleichzeitig lernen und leben wollen</li>
        </ul>
      </section>
    </div>
  </main>
</body>
</html>
```